Neighbourhood assistance

I need an app design for a social idea. Each person has some skils and could offer some assistance to some of his neighbours. With this app I will bring people together. For free or also for some money.That doesn't matter.

Please have a look into my pptx file which should give you an idea about the upcoming app.

Social

```html
<!DOCTYPE html>
<html lang="de">
<head>
<meta charset="utf-8">
<title>Nachbarschaftshilfe – Registrierung</title>
<link href="https://fonts.googleapis.com/css2?family=Mulish:wght@400;600;700&display=swap" rel="stylesheet">
<style>
:root{
  --stage:#000;
  --screen-bg:#f2f2f2;
  --field-bg:#fafafa;
  --field-line:#e3e3e3;
  --text:#333;
  --muted:#8a8a8a;
  --hint:#999;
  --blue:#3498db;
  --blue-dark:#2a7fba;
  --nav:#2d7fc0;
  --orange:#e67e22;
  --orange-dark:#d35400;
  --green:#2ecc71;
  --green-dark:#27ae60;
  --indigo:#3b5998;
  --indigo-dark:#2d4679;
  --white:#fff;
}
*{box-sizing:border-box;margin:0;padding:0}
html,body{width:935px;height:1200px;overflow:hidden;background:var(--stage)}
body{position:relative;font-family:"Mulish",sans-serif;color:var(--text)}
.screen{position:absolute;width:212px;height:376px;background:var(--screen-bg);overflow:hidden}
.screen--welcome{left:72px;top:117px}
.screen--mail{left:364px;top:122px}
.screen--thanks{left:670px;top:122px}
.screen--interests{left:68px;top:688px}
.screen--profile{left:364px;top:690px}

.status-bar{position:absolute;left:0;top:0;width:100%;height:14px;font-size:7px;font-weight:600;display:flex;align-items:center;padding:0 4px;color:var(--text)}
.status-bar .carrier{flex:1;display:flex;align-items:center;gap:4px}
.status-bar .time{position:absolute;left:0;right:0;text-align:center}
.status-bar .battery{display:flex;align-items:center;gap:2px;margin-left:auto}
.nav-bar{position:absolute;left:0;top:0;width:100%;height:44px;background:var(--nav);color:var(--white)}
.nav-bar .status-bar{color:var(--white)}
.nav-title{position:absolute;top:14px;left:0;right:0;height:30px;line-height:30px;text-align:center;font-size:10px;font-weight:700}
.nav-back{position:absolute;left:6px;top:22px}

.headline{position:absolute;left:0;right:0;top:86px;text-align:center;font-size:11px;font-weight:700}
.message{position:absolute;left:0;right:0;top:132px;text-align:center;font-size:11.5px;line-height:14px}

.btn{position:absolute;left:17px;width:178px;height:32px;border-radius:2px;display:flex;color:var(--white);font-size:9px;font-weight:600;overflow:hidden}
.btn .btn-icon{width:32px;height:100%;display:flex;align-items:center;justify-content:center}
.btn .btn-label{flex:1;display:flex;align-items:center;justify-content:center;padding-right:10px}
.btn--orange{background:var(--orange)}.btn--orange .btn-icon{background:var(--orange-dark)}
.btn--green{background:var(--green)}.btn--green .btn-icon{background:var(--green-dark)}
.btn--indigo{background:var(--indigo)}.btn--indigo .btn-icon{background:var(--indigo-dark)}
.btn--blue{background:var(--blue)}.btn--blue .btn-icon{background:var(--blue-dark)}

.field{position:absolute;height:32px;background:var(--field-bg);border:1px solid var(--field-line);border-radius:2px;font-size:8.5px;color:#555;display:flex;align-items:center;padding-left:7px}
.field--icon{left:17px;width:178px}
.field--icon .field-icon{width:16px;display:flex;justify-content:center}
.field--icon .field-sep{width:1px;height:11px;background:#ccc;transform:skewX(-25deg);margin:0 10px 0 6px}
.field--icon .field-label{flex:1;text-align:left;padding-left:20px}

.fine-print{position:absolute;left:20px;top:288px;width:185px;font-size:7.5px;line-height:11px;color:var(--hint);white-space:nowrap}

.cover{position:absolute;left:0;top:44px;width:100%;height:65px;background:linear-gradient(180deg,#6f8ea3 0%,#8fa08a 45%,#3f4a3a 80%,#1c1f1c 100%)}
.avatar{position:absolute;left:68px;top:68px;width:66px;height:66px;border-radius:50%;border:3px solid var(--blue);background:var(--white);padding:2px}
.avatar-fill{width:100%;height:100%;border-radius:50%;background:linear-gradient(180deg,#c9d3dc,#6d7681)}
</style>
</head>
<body>

<!-- Welcome -->
<section class="screen screen--welcome">
  <div class="status-bar">
    <span class="carrier">●●●○○ Kelvo
      <svg width="8" height="6" viewBox="0 0 8 6"><path d="M4 6 1 2.6a4.4 4.4 0 0 1 6 0Z" fill="currentColor"/></svg></span>
    <span class="time">4:21 PM</span>
    <span class="battery">100% <svg width="14" height="6" viewBox="0 0 14 6"><rect x=".5" y=".5" width="11.5" height="5" rx="1" fill="currentColor" stroke="currentColor"/><rect x="12.5" y="2" width="1.3" height="2" fill="currentColor"/></svg></span>
  </div>
  <h1 class="headline">Du bist mit dabei!</h1>
  <a class="btn btn--orange" style="top:123px">
    <span class="btn-icon"><svg width="10" height="8" viewBox="0 0 10 8"><rect width="10" height="8" rx="1" fill="#fff"/><path d="M0 1 5 4.5 10 1" fill="none" stroke="#d35400" stroke-width="1"/></svg></span>
    <span class="btn-label">Per Mail registrieren</span></a>
  <a class="btn btn--green" style="top:169px">
    <span class="btn-icon"><svg width="7" height="11" viewBox="0 0 7 11"><rect x=".6" y=".6" width="5.8" height="9.8" rx="1" fill="none" stroke="#fff" stroke-width="1.2"/><circle cx="3.5" cy="8.8" r=".7" fill="#fff"/></svg></span>
    <span class="btn-label">Per Smartphone registrieren</span></a>
  <a class="btn btn--indigo" style="top:216px">
    <span class="btn-icon"><svg width="8" height="8" viewBox="0 0 8 8"><rect width="8" height="8" fill="#fff"/></svg></span>
    <span class="btn-label">Per Friendnet registrieren</span></a>
  <a class="btn btn--blue" style="top:310px">
    <span class="btn-icon"><svg width="9" height="10" viewBox="0 0 9 10"><path d="M2 4.5V3a2.5 2.5 0 0 1 5 0v1.5" fill="none" stroke="#fff" stroke-width="1.3"/><rect y="4.3" width="9" height="5.7" rx="1" fill="#fff"/></svg></span>
    <span class="btn-label">Einloggen</span></a>
</section>

<!-- Register by mail -->
<section class="screen screen--mail">
  <header class="nav-bar">
    <div class="status-bar">
      <span class="carrier">●●●○○ Kelvo
        <svg width="8" height="6" viewBox="0 0 8 6"><path d="M4 6 1 2.6a4.4 4.4 0 0 1 6 0Z" fill="currentColor"/></svg></span>
      <span class="time">4:21 PM</span>
      <span class="battery">100% <svg width="14" height="6" viewBox="0 0 14 6"><rect x=".5" y=".5" width="11.5" height="5" rx="1" fill="currentColor" stroke="currentColor"/><rect x="12.5" y="2" width="1.3" height="2" fill="currentColor"/></svg></span>
    </div>
    <div class="nav-title">Per Mail registrieren</div>
  </header>
  <label class="field field--icon" style="top:134px">
    <span class="field-icon"><svg width="9" height="7" viewBox="0 0 9 7"><rect width="9" height="7" rx="1" fill="#bbb"/><path d="M0 1 4.5 4 9 1" fill="none" stroke="#fafafa" stroke-width=".9"/></svg></span>
    <span class="field-sep"></span><span class="field-label">E-Mail-Adresse?</span></label>
  <label class="field field--icon" style="top:181px">
    <span class="field-icon"><svg width="8" height="9" viewBox="0 0 9 10"><path d="M2 4.5V3a2.5 2.5 0 0 1 5 0v1.5" fill="none" stroke="#bbb" stroke-width="1.3"/><rect y="4.3" width="9" height="5.7" rx="1" fill="#bbb"/></svg></span>
    <span class="field-sep"></span><span class="field-label">Passwort?</span></label>
  <a class="btn btn--blue" style="top:231px;height:33px">
    <span class="btn-icon"><svg width="10" height="10" viewBox="0 0 10 10"><path d="M5 1H1v8h8V5" fill="none" stroke="#fff" stroke-width="1.1"/><path d="M4 6.2 4.3 4.6 8.3.6l1.1 1.1-4 4Z" fill="#fff"/></svg></span>
    <span class="btn-label">Registrieren</span></a>
  <p class="fine-print">*indem du auf Registrieren tippst,<br>akzeptierst du die Geschäftsbedingungen</p>
</section>

<!-- Thanks -->
<section class="screen screen--thanks">
  <header class="nav-bar">
    <div class="status-bar">
      <span class="carrier">●●●○○ Kelvo
        <svg width="8" height="6" viewBox="0 0 8 6"><path d="M4 6 1 2.6a4.4 4.4 0 0 1 6 0Z" fill="currentColor"/></svg></span>
      <span class="time">4:21 PM</span>
      <span class="battery">100% <svg width="14" height="6" viewBox="0 0 14 6"><rect x=".5" y=".5" width="11.5" height="5" rx="1" fill="currentColor" stroke="currentColor"/><rect x="12.5" y="2" width="1.3" height="2" fill="currentColor"/></svg></span>
    </div>
    <svg class="nav-back" width="7" height="12" viewBox="0 0 7 12"><path d="M6 1 1 6l5 5" fill="none" stroke="#fff" stroke-width="1.3"/></svg>
    <div class="nav-title">Danke</div>
  </header>
  <p class="message">Bitte Mail Konto checken und<br>Link bestätigen!</p>
  <a class="btn btn--blue" style="top:201px;left:18px;height:33px">
    <span class="btn-icon"><svg width="14" height="10" viewBox="0 0 14 10"><rect width="11" height="8" rx="1" fill="#fff"/><path d="M0 1 5.5 4.5 11 1" fill="none" stroke="#2a7fba" stroke-width="1"/><circle cx="11" cy="7.5" r="2.5" fill="#fff" stroke="#2a7fba" stroke-width=".8"/><path d="m9.9 7.5.8.8 1.4-1.5" fill="none" stroke="#2a7fba" stroke-width=".8"/></svg></span>
    <span class="btn-label">Mail bestätigt</span></a>
</section>

<!-- Interests -->
<section class="screen screen--interests">
  <header class="nav-bar">
    <div class="status-bar">
      <span class="carrier">●●●○○ Kelvo
        <svg width="8" height="6" viewBox="0 0 8 6"><path d="M4 6 1 2.6a4.4 4.4 0 0 1 6 0Z" fill="currentColor"/></svg></span>
      <span class="time">4:21 PM</span>
      <span class="battery">100% <svg width="14" height="6" viewBox="0 0 14 6"><rect x=".5" y=".5" width="11.5" height="5" rx="1" fill="currentColor" stroke="currentColor"/><rect x="12.5" y="2" width="1.3" height="2" fill="currentColor"/></svg></span>
    </div>
    <svg class="nav-back" width="7" height="12" viewBox="0 0 7 12"><path d="M6 1 1 6l5 5" fill="none" stroke="#fff" stroke-width="1.3"/></svg>
    <div class="nav-title">Interessen</div>
  </header>
  <label class="field" style="top:133px;left:17px;width:178px;padding-left:11px">Du bietest an...</label>
  <label class="field" style="top:181px;left:17px;width:178px;padding-left:11px">Du brauchst...</label>
  <a class="btn btn--blue" style="top:281px;height:33px">
    <span class="btn-icon"><svg width="9" height="10" viewBox="0 0 9 10"><circle cx="4.5" cy="2.6" r="2.4" fill="#fff"/><path d="M0 10a4.5 4 0 0 1 9 0Z" fill="#fff"/></svg></span>
    <span class="btn-label">Profil anpassen</span></a>
</section>

<!-- Profile -->
<section class="screen screen--profile">
  <header class="nav-bar">
    <div class="status-bar">
      <span class="carrier">●●●○○ Kelvo
        <svg width="8" height="6" viewBox="0 0 8 6"><path d="M4 6 1 2.6a4.4 4.4 0 0 1 6 0Z" fill="currentColor"/></svg></span>
      <span class="time">4:21 PM</span>
      <span class="battery">100% <svg width="14" height="6" viewBox="0 0 14 6"><rect x=".5" y=".5" width="11.5" height="5" rx="1" fill="currentColor" stroke="currentColor"/><rect x="12.5" y="2" width="1.3" height="2" fill="currentColor"/></svg></span>
    </div>
    <svg class="nav-back" width="7" height="12" viewBox="0 0 7 12"><path d="M6 1 1 6l5 5" fill="none" stroke="#fff" stroke-width="1.3"/></svg>
    <div class="nav-title">Profil anpassen</div>
  </header>
  <div class="cover" role="img" aria-label="Titelbild: neblige Hügellandschaft mit Bäumen"></div>
  <div class="avatar"><div class="avatar-fill" role="img" aria-label="Profilfoto des Nutzers"></div></div>
  <label class="field" style="top:143px;left:8px;width:94px;height:33px">Name</label>
  <label class="field" style="top:143px;left:108px;width:95px;height:33px">Vorname</label>
  <label class="field" style="top:189px;left:8px;width:157px;height:33px">Strasse</label>
  <label class="field" style="top:189px;left:171px;width:32px;height:33px">Nr</label>
  <label class="field" style="top:236px;left:8px;width:45px;height:33px">PLZL</label>
  <label class="field" style="top:236px;left:60px;width:143px;height:33px">Ort</label>
  <label class="field" style="top:282px;left:8px;width:195px;height:33px">Land</label>
  <a class="btn btn--blue" style="top:330px;left:8px;width:195px;height:33px">
    <span class="btn-icon"><svg width="10" height="10" viewBox="0 0 10 10"><path d="M.6.6h7l1.8 1.8v7H.6Z" fill="none" stroke="#fff" stroke-width="1.1"/><rect x="2.5" y="1" width="4" height="2.6" fill="#fff"/><rect x="2.3" y="5.8" width="5.4" height="3" fill="#fff"/></svg></span>
    <span class="btn-label">Speichern</span></a>
</section>

</body>
</html>
```